The Bright Path Foundation

This is a non profit . We are a 501(c)(3) charitable organization in the United States. The organization is a volunteer based group providing basic healthcare to those living in underserved rural areas around the world. I have attached a brochure that provides some information about the organization. We are looking for a basic 5 page web page Page 1 Photos that fade into the next x 3 with mission statementPage 2 About us - details about bright path foundation. also introducing our Founders of the organization. Marlene Quist, M.D. Doria Lemke , FNP, Paula Dweck, FNP, Brent Lomax. ( will provide you info on each.Page 3 Projects coming up and futurePage 4 Get involved - Give a donation, Volunteer, Corporate supportPage 5 Support us and contact us with a message box.We mainly work in South America but anticipate trave to South Africa in the near future. Colors bright with emphasis on Reds and Purples. I have attached some photos and ideas. You can use or not use ok to use something similar if you so like

Target Market(s)

People interested in volunteering time or money to overseas medical work. NOT a religious base

Colors
876aae
ec1f27
f37022
9bcb3c

Requirements
Must have
• Colorful pictures nature, brings out emotion, colorful, children from various parts of the world, animals.
• Tried to down load some pictures but would not go thru.

```html
<!DOCTYPE html>
<html lang="en">
<head>
<meta charset="utf-8">
<title>Bright Path Foundation</title>
<link href="https://fonts.googleapis.com/css2?family=Cinzel:wght@700&family=Lato:wght@400;700&family=Poppins:wght@400;500&display=swap" rel="stylesheet">
<style>
:root{
  --orange:#f37022;
  --red:#ec1f27;
  --purple:#876aae;
  --purple-deep:#7a5a98;
  --purple-light:#b88cc4;
  --green:#9bcb3c;
  --dark:#2b2b2d;
  --text:#8a8a8a;
  --white:#fff;
}
*{margin:0;padding:0;box-sizing:border-box}
html,body{width:1200px;height:3510px;overflow:hidden;background:#fff}
body{position:relative;font-family:'Lato',sans-serif;color:var(--text)}
.abs{position:absolute}
.topbar{left:0;top:0;width:1200px;height:52px;background:var(--orange)}
.topbar .social{position:absolute;left:78px;top:0;display:flex;height:52px}
.topbar .social span{width:52px;height:52px;border-left:1px solid rgba(255,255,255,.35);display:flex;align-items:center;justify-content:center}
.topbar .social span:last-child{border-right:1px solid rgba(255,255,255,.35)}
.topbar .social i{width:12px;height:12px;border-radius:50%;background:#fff;display:block}
.topbar .contact{position:absolute;right:78px;top:0;height:52px;display:flex;color:#fff;font-size:15px}
.topbar .contact div{display:flex;align-items:center;gap:10px;padding:0 16px;border-left:1px solid rgba(255,255,255,.35)}
.topbar .contact div:last-child{border-right:1px solid rgba(255,255,255,.35)}
.nav{left:0;top:52px;width:1200px;height:105px;background:#fff}
.nav a{position:absolute;top:44px;font-size:16px;color:#8a8a8a;text-decoration:none}
.nav a.active{color:var(--green)}
.nav a.active:after{content:"";position:absolute;left:50%;top:26px;margin-left:-6px;border:6px solid transparent;border-bottom:9px solid var(--green);border-top:0}
.brand{display:flex;align-items:center;gap:8px;font-family:'Lato',sans-serif;font-weight:700;color:var(--purple);font-size:21px;white-space:nowrap}
.brand i{width:22px;height:22px;border-radius:50%;background:var(--purple);display:block}
.hero{left:0;top:157px;width:1200px;height:623px;background:linear-gradient(180deg,#2e4a7a 0%,#5a6f8d 30%,#8a7a55 55%,#9c7c45 100%)}
.hero-title{left:79px;top:276px;font-family:'Cinzel',serif;font-size:50px;line-height:58px;color:#fff;font-weight:700}
.hero-text{left:79px;top:404px;width:480px;font-size:18px;line-height:25px;color:#fff}
.btn{display:inline-flex;align-items:center;justify-content:center;border-radius:26px;font-family:'Poppins',sans-serif;font-size:16px;color:#fff;background:var(--purple)}
.btn.ghost{background:none;border:2px solid #fff}
.card{top:688px;width:332px;height:290px;color:#fff;text-align:center}
.card svg{margin-top:38px}
.card h3{font-family:'Poppins',sans-serif;font-weight:400;font-size:23px;margin-top:14px}
.card p{font-size:13.5px;line-height:23px;margin:12px 16px 0}
.frame{left:78px;top:1042px;width:519px;height:497px;background:#fff;box-shadow:0 0 6px rgba(0,0,0,.12)}
.frame .photo{position:absolute;left:10px;top:10px;width:499px;height:477px;background:linear-gradient(135deg,#8a6a5a,#c83a5a 45%,#6a4a8a 75%,#b87a4a)}
.about-icon{left:680px;top:1042px;width:80px;height:80px;border-radius:50%;background:var(--purple)}
.section-title{font-family:'Cinzel',serif;font-weight:700;color:#1a1a1a}
.about-text{left:679px;top:1214px;width:440px;font-size:13px;line-height:27px;color:#8a8a8a}
.phone-big{left:855px;top:1490px;display:flex;align-items:center;gap:16px;font-family:'Poppins',sans-serif;font-size:28px;color:#333}
.mission-bg{left:0;top:1614px;width:700px;height:624px;background:linear-gradient(160deg,#3a3a3c,#1e1e20 60%,#2a2420)}
.mission-photo{left:700px;top:1614px;width:500px;height:624px;background:linear-gradient(150deg,#e8efe0,#7aa64a 45%,#3f8a3a 70%,#2a4a8a)}
.mission-frame{left:78px;top:1698px;width:1044px;height:457px;border:6px solid var(--orange)}
.mission-text{left:131px;top:1812px;width:510px;font-size:13.5px;line-height:27px;color:#e8e8e8}
.tile{position:absolute;width:343px;height:260px}
.news{left:0;top:2977px;width:1200px;height:104px;background:var(--purple-deep)}
.footer{left:0;top:3081px;width:1200px;height:429px;background:var(--dark)}
.footer-links{left:0;top:3268px;width:1200px;text-align:center;font-size:14px;color:#fff}
.footer-links span{margin:0 22px;color:#bbb}
.circle{position:absolute;width:46px;height:46px;border-radius:50%}
</style>
</head>
<body>

<header class="abs topbar">
  <div class="social"><span><i></i></span><span><i></i></span><span><i></i></span><span><i></i></span></div>
  <div class="contact">
    <div><svg width="18" height="18" viewBox="0 0 24 24" fill="none" stroke="#fff" stroke-width="1.6"><path d="M5 3h4l2 5-3 2a12 12 0 0 0 6 6l2-3 5 2v4a2 2 0 0 1-2 2A18 18 0 0 1 3 5a2 2 0 0 1 2-2z"/></svg>1-555-014-2290</div>
    <div><svg width="20" height="16" viewBox="0 0 24 18" fill="none" stroke="#fff" stroke-width="1.6"><rect x="1" y="1" width="22" height="16"/><path d="M1 1l11 9 11-9"/></svg>info@brightpathfdn.org</div>
  </div>
</header>

<nav class="abs nav">
  <a class="active" style="left:184px">Home</a>
  <a style="left:273px">About Us</a>
  <a style="left:387px">Projects</a>
  <div class="brand abs" style="left:492px;top:40px"><i></i>Bright Path Foundation</div>
  <a style="left:757px">Get Involved</a>
  <a style="left:898px">Blog</a>
  <a style="left:981px">Contact Us</a>
</nav>

<section class="abs hero" role="img" aria-label="Two women in colourful woven shawls and hats looking over golden fields toward blue mountains"></section>
<h1 class="abs hero-title">TOGETHER WE CAN<br>MAKE A DIFFERENCE</h1>
<p class="abs hero-text">Your donations allow us to provide medical care, health resources and supplies, and wellness education to the communities we serve.</p>
<a class="abs btn" style="left:78px;top:500px;width:145px;height:50px">Donate Now</a>
<a class="abs btn ghost" style="left:234px;top:500px;width:145px;height:50px">Read More</a>

<div class="abs card" style="left:78px;background:var(--green)">
  <svg width="82" height="82" viewBox="0 0 82 82" fill="none" stroke="#fff" stroke-width="2.5"><rect x="4" y="40" width="74" height="38" rx="3"/><path d="M4 40l10-14h54l10 14"/><circle cx="41" cy="20" r="15"/><path d="M41 11v18M46 15h-7a3 3 0 0 0 0 6h4a3 3 0 0 1 0 6h-8"/></svg>
  <h3>Give a donation</h3>
  <p>Lorem ipsum dolor sit amet, consectetur adipiscing elit, sed eiusmod tempor incididunt labore et dolore magna aliqua.</p>
</div>
<div class="abs card" style="left:433px;background:var(--red)">
  <svg width="84" height="84" viewBox="0 0 84 84" fill="none" stroke="#fff" stroke-width="2.5"><circle cx="42" cy="42" r="28"/><circle cx="42" cy="42" r="12"/><circle cx="42" cy="38" r="4"/><circle cx="18" cy="16" r="7"/><circle cx="66" cy="16" r="7"/><circle cx="18" cy="68" r="7"/><circle cx="66" cy="68" r="7"/></svg>
  <h3>Volunteer</h3>
  <p>Lorem ipsum dolor sit amet, consectetur adipiscing elit, sed eiusmod tempor incididunt labore et dolore magna aliqua.</p>
</div>
<div class="abs card" style="left:790px;background:var(--purple)">
  <svg width="82" height="82" viewBox="0 0 82 82" fill="none" stroke="#fff" stroke-width="2.5"><circle cx="41" cy="24" r="14"/><path d="M25 24a16 16 0 0 1 32 0M26 22v8M56 22v8"/><path d="M8 80V64a14 14 0 0 1 14-14h38a14 14 0 0 1 14 14v16z"/><path d="M36 50l5 14 5-14"/></svg>
  <h3>Corporate support</h3>
  <p>Lorem ipsum dolor sit amet, consectetur adipiscing elit, sed eiusmod tempor incididunt labore et dolore magna aliqua.</p>
</div>

<div class="abs frame"><div class="photo" role="img" aria-label="Smiling woman in a bright traditional hat and shawl holding a young child at a textile market"></div></div>
<div class="abs about-icon"></div>
<h2 class="abs section-title" style="left:679px;top:1140px;font-size:44px">ABOUT US</h2>
<p class="abs about-text">Lorem ipsum dolor sit amet, consectetur adipiscing elit, sed do theye eiusmod tempor incididunt ut labore et dolore magna aliqua. Ut enim ad minim veniam, quis nostrud exercitation ullamco laboris nisi ut toe aliquip ex ea commodo consequat. Duis aute irure dolor in the more reprehenderit in voluptate velit esse cillum dolore eu fugiat nulla tho pariatur. Excepteur sint occaecat cupidatat non proident, sunt in ofe culpa qui officia deserunt mollit anim id est laborum. It w popularised in the 1960s with the release of Letraset sheets containing Lo Ipsum passages, and more recently with desktop publishing software.</p>
<a class="abs btn" style="left:677px;top:1489px;width:146px;height:50px">Read More</a>
<div class="abs phone-big"><svg width="42" height="42" viewBox="0 0 24 24" fill="none" stroke="var(--purple)" stroke-width="1.6"><path d="M5 3h4l2 5-3 2a12 12 0 0 0 6 6l2-3 5 2v4a2 2 0 0 1-2 2A18 18 0 0 1 3 5a2 2 0 0 1 2-2z"/><path d="M15 2a7 7 0 0 1 7 7M15 6a3 3 0 0 1 3 3"/></svg>1-555-014-2290</div>

<section class="abs mission-bg" role="img" aria-label="Dimmed photo of a community gathering"></section>
<section class="abs mission-photo" role="img" aria-label="Smiling children carrying a green recycling bin full of plastic bottles outdoors"></section>
<div class="abs mission-frame"></div>
<h2 class="abs section-title" style="left:131px;top:1744px;font-size:40px;color:#fff">OUR MISSION</h2>
<p class="abs mission-text">The Bright Path Foundation was founded with the aim of helping rural and indigenous individuals in various parts of the world. The Foundation's vision is to see that every woman, man and child have access to basic medical care and treatment as well as fundamental knowledge in preventative care. There are many people living in regions of the world today who have limited or no access to health centers. Often, these individuals travel hours and in many instances days for basic care that often times can be averted with preventative care measures.</p>
<a class="abs btn" style="left:129px;top:2051px;width:146px;height:51px">Read More</a>

<h2 class="abs section-title" style="left:0;width:1200px;text-align:center;top:2296px;font-size:42px">PROJECT GALLERY</h2>
<div class="tile" style="left:78px;top:2363px;background:linear-gradient(135deg,#3a2a22,#7a5a40)" role="img" aria-label="Child resting head on hand at a school desk"></div>
<div class="tile" style="left:428px;top:2363px;background:linear-gradient(135deg,#4a3a2e,#8a7a66)" role="img" aria-label="Children raising hands behind a brick wall"></div>
<div class="tile" style="left:779px;top:2363px;background:linear-gradient(135deg,#2a2624,#5a4a40)" role="img" aria-label="Girl writing on a chalkboard"></div>
<div class="tile" style="left:78px;top:2630px;background:linear-gradient(135deg,#3a2a3a,#b8324a)" role="img" aria-label="Women in headscarves with a child in a clinic"></div>
<div class="tile" style="left:428px;top:2630px;background:linear-gradient(135deg,#6a5a4a,#b8a080)" role="img" aria-label="Volunteer teaching children in a classroom"></div>
<div class="tile" style="left:779px;top:2630px;background:linear-gradient(135deg,#8a8a80,#5a4a40)" role="img" aria-label="Volunteer smiling with two young girls"></div>

<section class="abs news">
  <div class="abs" style="left:79px;top:28px;font-family:'Lato',sans-serif;font-size:42px;color:#fff;letter-spacing:1px">NEWSLETTER</div>
  <div class="abs" style="left:498px;top:26px;width:481px;height:52px;background:var(--purple-light);color:#fff;font-size:13px;padding:18px 14px">Enter Email Id</div>
  <div class="abs" style="left:979px;top:26px;width:143px;height:52px;background:#fff;color:var(--purple-deep);font-family:'Poppins',sans-serif;font-size:16px;display:flex;align-items:center;justify-content:center">Subscribe</div>
</section>

<footer class="abs footer"></footer>
<div class="brand abs" style="left:492px;top:3196px"><i></i>Bright Path Foundation</div>
<div class="abs footer-links">Home<span>|</span>About Us<span>|</span>Projects<span>|</span>Get Involved<span>|</span>Contact Us</div>
<div class="circle" style="left:548px;top:3314px;background:#4a6ab8"></div>
<div class="circle" style="left:606px;top:3314px;background:#d8407a"></div>
<div class="abs" style="left:0;top:3416px;width:1200px;height:1px;background:#3d3d40"></div>
<div class="abs" style="left:0;top:3453px;width:1200px;text-align:center;font-size:12px;color:#999">Copyright © <b style="color:#ddd">BRIGHT PATH FOUNDATION</b> - 2019 . All Right Reserved</div>

</body>
</html>
```